BW Business Card

Used Car Sales
We are trying to recreate the image of our license plate on business cards,
it is a red background with a white oval that is open on the ends
I attempted to upload the image but it was a dismal failure when the products arrived
the lettering was too small and the edges were white
I think maybe the red needs some texture in it, still red but something that doesn't look so flat
and maybe a beveled edge around the white (not sure)

Target Market(s)

Adults 25-65 that drive

Industry/Entity Type

Business

Contact Information for Business Card

Darlene Whitcombe, Sales Manager, BRIGHTWAY AUTO MART, INC., 462 Fernhill Road, Cedar Hollow, MO 38478,
272 587-2064 (office), 272 587-6259 (fax) - We Finance everyone with approved credit
BrightwayAutoMart.Com

On Back: Financing Available - We Finance everyone with approved credit
Easy Payments: Monthly, Semi-Monthly or Weekly
Ask about our Layaway plan
Open Mon-Sat
8:30 AM - 5 PM

Requirements
Must have
• We want to match the license plate (minus holes for screws)

```html
<!DOCTYPE html>
<html lang="en">
<head>
<meta charset="utf-8">
<title>Brightway Auto Mart – Business Card</title>
<link href="https://fonts.googleapis.com/css2?family=Archivo:wght@700;800;900&family=Arimo:wght@400;700&display=swap" rel="stylesheet">
<style>
  :root {
    --backdrop: #2b2b2b;
    --card: #ffffff;
    --brand-red: #a01c22;
    --ink: #2e2e2e;
    --ink-soft: #3a3a3a;
    --rim: #d9b98f;
  }
  * { margin: 0; padding: 0; box-sizing: border-box; }
  html, body { width: 1200px; height: 1000px; overflow: hidden; }
  body { background: var(--backdrop); font-family: "Arimo", Arial, sans-serif; position: relative; }

  .card { position: absolute; background: var(--card); overflow: hidden; box-shadow: 0 6px 18px rgba(0,0,0,.55); }
  .card--front { left: 52px; top: 46px; width: 695px; height: 406px; }
  .card--back  { left: 442px; top: 513px; width: 703px; height: 412px; }
  .plate { position: absolute; inset: 0; width: 100%; height: 100%; }
  .card > div, .card > p { position: absolute; }

  .person__name { left: 33px; top: 26px; font-family: "Archivo", Arial, sans-serif; font-weight: 800; font-size: 31px; color: var(--brand-red); letter-spacing: .2px; }
  .person__role { left: 34px; top: 64px; font-size: 22px; color: var(--ink-soft); letter-spacing: 1px; }

  .company { right: 31px; top: 30px; width: 215px; text-align: right; }
  .company__name { font-family: "Archivo", Arial, sans-serif; font-weight: 800; font-size: 21px; line-height: 24px; letter-spacing: 1px; color: var(--ink); border-bottom: 1.5px solid var(--brand-red); padding-bottom: 3px; white-space: nowrap; }
  .contact { display: flex; justify-content: space-between; margin-top: 3px; font-size: 10.5px; line-height: 13px; color: var(--ink); letter-spacing: .4px; }
  .contact__label { color: var(--brand-red); font-weight: 700; font-size: 9.5px; text-align: left; }

  .offer { left: 0; width: 695px; top: 158px; text-align: center; }
  .offer__headline { font-family: "Archivo", Arial, sans-serif; font-weight: 800; font-size: 37px; line-height: 40px; letter-spacing: 2.5px; color: var(--brand-red); }
  .offer__line { font-family: "Archivo", Arial, sans-serif; font-weight: 700; font-size: 18.5px; color: var(--ink); }
  .offer__url { font-size: 18px; letter-spacing: 1.1px; color: var(--ink); margin-top: 2px; }
  .offer__url span, .back-url span, .layaway span { color: var(--brand-red); }

  .finance { left: 0; width: 703px; top: 80px; text-align: center; }
  .finance__headline { font-family: "Archivo", Arial, sans-serif; font-weight: 800; font-size: 35px; letter-spacing: .4px; color: var(--brand-red); line-height: 42px; }
  .terms { display: flex; justify-content: space-between; width: 432px; margin: 6px auto 0; font-family: "Archivo", Arial, sans-serif; font-weight: 700; font-size: 17px; color: var(--ink); }
  .layaway { font-family: "Archivo", Arial, sans-serif; font-weight: 700; font-size: 17px; letter-spacing: 6.4px; color: var(--ink); margin-top: 15px; }
  .hours { font-family: "Archivo", Arial, sans-serif; font-weight: 800; font-size: 32px; letter-spacing: 1px; color: var(--ink); margin-top: 8px; word-spacing: 4px; }
  .back-url { left: 0; width: 703px; bottom: 5px; text-align: center; font-family: "Archivo", Arial, sans-serif; font-weight: 700; font-size: 15px; letter-spacing: .6px; color: var(--ink); }
</style>
</head>
<body>

<section class="card card--front">
  <svg class="plate" viewBox="0 0 695 406" aria-hidden="true">
    <defs>
      <linearGradient id="frontRed" x1="0" y1="0" x2="1" y2="0">
        <stop offset="0" stop-color="#8e161b"/>
        <stop offset=".55" stop-color="#a31d23"/>
        <stop offset="1" stop-color="#560a0c"/>
      </linearGradient>
      <linearGradient id="frontCity" x1="0" y1="0" x2="0" y2="1">
        <stop offset="0" stop-color="#c2474b"/>
        <stop offset="1" stop-color="#f4f4f4"/>
      </linearGradient>
    </defs>
    <path d="M0 186 Q347.5 406 695 186 L695 406 L0 406 Z" fill="url(#frontRed)"/>
    <path d="M0 186 Q347.5 406 695 186" fill="none" stroke="var(--rim)" stroke-width="1.5"/>
    <rect x="0" y="382" width="695" height="24" fill="#fff"/>
    <rect x="82" y="290" width="512" height="92" fill="url(#frontCity)" role="img" aria-label="White city skyline silhouette"/>
  </svg>

  <p class="person__name">Darlene Whitcombe</p>
  <p class="person__role">Sales Manager</p>

  <div class="company">
    <p class="company__name">BRIGHTWAY<br>AUTO MART, INC.</p>
    <div class="contact"><span class="contact__label">Adress:</span><span>462 Fernhill Road<br>Cedar Hollow, MO</span></div>
    <div class="contact"><span class="contact__label">Phone:</span><span>(office) 272 587-2064<br>(fax) 272 587-6259</span></div>
  </div>

  <div class="offer">
    <p class="offer__headline">WE FINANCE</p>
    <p class="offer__line">Everyone with approved credit!</p>
    <p class="offer__url">www.<span>BrightwayAutoMart</span>.com</p>
  </div>
</section>

<section class="card card--back">
  <svg class="plate" viewBox="0 0 703 412" aria-hidden="true">
    <defs>
      <linearGradient id="backRed" x1="0" y1="0" x2="1" y2="0">
        <stop offset="0" stop-color="#8e161b"/>
        <stop offset=".55" stop-color="#a31d23"/>
        <stop offset="1" stop-color="#560a0c"/>
      </linearGradient>
      <linearGradient id="backCity" x1="0" y1="0" x2="0" y2="1">
        <stop offset="0" stop-color="#c2474b"/>
        <stop offset="1" stop-color="#f4f4f4"/>
      </linearGradient>
    </defs>
    <path d="M0 190 Q351.5 408 703 190 L703 412 L0 412 Z" fill="url(#backRed)"/>
    <path d="M0 190 Q351.5 408 703 190" fill="none" stroke="var(--rim)" stroke-width="1.5"/>
    <rect x="0" y="388" width="703" height="24" fill="#fff"/>
    <rect x="84" y="292" width="516" height="96" fill="url(#backCity)" role="img" aria-label="White city skyline silhouette"/>
  </svg>

  <div class="finance">
    <p class="finance__headline">FINANCING AVAILABLE</p>
    <div class="terms"><span>Monthly</span><span>-</span><span>Semi-Monthly</span><span>-</span><span>Weekly</span></div>
    <p class="layaway">Ask about our <span>Lay Away</span> plan!</p>
    <p class="hours">Mon - Sat &nbsp;8:30AM - 5PM</p>
  </div>

  <p class="back-url">www.<span>BrightwayAutoMart</span>.com</p>
</section>

</body>
</html>
```